New Business Card Design Project

I need a design for business cards, i am an electrical business called "Tandor Electrical and Communications" i need the cards to be double sided with the company logo on the back (attached) the front needs to say my company name, web site, email address, telephone number, and ABN number and electrical license number. I am open to different arrangements of the information but would like the background to be incorporating something electrical or something that looks smart. open to all additional ideas also.

The company colours are orange and grey see logo attached.

Business Name: Tandor Electrical and Communications
Website: tandorelectricalandcomms.example.au
Email: brent@tandorelectricalandcomms.example.au
Telephone(mobile): 0481203967
ABN: 71829034618
Lic No: 830472F

Target Market(s)

Business entities, Project Managers, Accounts, Clients

Industry/Entity Type

Electrician

Contact Information for Business Card

I need a design for business cards, i am an electrical business called "Tandor Electrical and Communications" i need the cards to be double sided with the company logo on the back (attached) the front needs to say my company name

Font styles to use
Serif
Sans Serif

Colors
f37122
5c5c5c

Requirements
Must have
• Must have the Logo on the back open to different ways of it being on the back but had in mind to keep it central but again open to other options
Nice to have
• A real modern cool background that is eye catching yet contemporary
Should not have
• No backgrounds of a light bulb or plug or anything like that

```html
<!DOCTYPE html>
<html lang="en">
<head>
<meta charset="utf-8">
<title>Tandor Electrical and Communications – Business Cards</title>
<link href="https://fonts.googleapis.com/css2?family=Open+Sans:wght@400;600&display=swap" rel="stylesheet">
<style>
  :root {
    --backdrop: #2a2a2a;
    --card-dark: #5c5c5c;
    --card-light: #ffffff;
    --brand-orange: #f4a11d;
    --brand-grey: #5c5c5c;
    --ink: #2b2b2b;
  }
  * { margin: 0; padding: 0; box-sizing: border-box; }
  html, body { width: 1200px; height: 1200px; overflow: hidden; }
  body {
    background: var(--backdrop);
    font-family: "Open Sans", Arial, sans-serif;
    position: relative;
  }
  .card {
    position: absolute;
    border-radius: 22px;
    box-shadow: 0 14px 30px rgba(0,0,0,0.45);
  }
  .card-back {
    left: 130px; top: 170px; width: 640px; height: 370px;
    background: var(--card-dark);
    display: flex; align-items: center; justify-content: center;
  }
  .card-back .brand-name {
    color: var(--card-light);
    font-weight: 600;
    font-size: 34px;
    letter-spacing: 1px;
    text-align: center;
    line-height: 1.25;
  }
  .card-front {
    left: 430px; top: 620px; width: 670px; height: 390px;
    background: var(--card-light);
  }
  .card-front .brand-name {
    position: absolute;
    right: 48px; top: 58px;
    color: var(--brand-orange);
    font-weight: 600;
    font-size: 30px;
    text-align: right;
    line-height: 1.25;
  }
  .card-front .rule {
    position: absolute;
    left: 270px; right: 40px; top: 168px;
    height: 3px; background: var(--brand-grey);
  }
  .contact-list {
    position: absolute;
    left: 280px; top: 186px;
    list-style: none;
    font-size: 15px;
    color: var(--ink);
  }
  .contact-list li { display: flex; align-items: center; gap: 10px; margin-bottom: 6px; }
  .contact-list svg { width: 15px; height: 15px; flex: none; }
  .registration {
    position: absolute;
    left: 262px; top: 296px;
    font-size: 15px; color: var(--ink);
    line-height: 1.6;
  }
  .registration .label { color: var(--brand-orange); }
</style>
</head>
<body>
  <section class="card card-back">
    <p class="brand-name">TANDOR<br>Electrical &amp; Communications</p>
  </section>

  <section class="card card-front">
    <p class="brand-name">TANDOR<br>Electrical &amp; Communications</p>
    <div class="rule"></div>
    <ul class="contact-list">
      <li>
        <svg viewBox="0 0 16 16"><circle cx="8" cy="8" r="7" fill="none" stroke="#f4a11d" stroke-width="1.5"/><path d="M1 8h14M8 1c3 3 3 11 0 14M8 1c-3 3-3 11 0 14" fill="none" stroke="#f4a11d" stroke-width="1.2"/></svg>
        tandorelectricalandcomms.example.au
      </li>
      <li>
        <svg viewBox="0 0 16 16"><rect x="1" y="3" width="14" height="10" rx="1.5" fill="#f4a11d"/><path d="M1.5 4l6.5 5 6.5-5" fill="none" stroke="#fff" stroke-width="1.3"/></svg>
        brent@tandorelectricalandcomms.example.au
      </li>
      <li>
        <svg viewBox="0 0 16 16"><circle cx="8" cy="8" r="8" fill="#f4a11d"/><path d="M5 4l2 2-1 1.2c.6 1.3 1.5 2.2 2.8 2.8L10 9l2 2-1.2 1.3C7.5 12 4 8.5 3.7 5.2z" fill="#fff"/></svg>
        0481203967
      </li>
    </ul>
    <p class="registration">
      <span class="label">ABN:</span> 71829034618<br>
      <span class="label">Lic No:</span> 830472F
    </p>
  </section>
</body>
</html>
```